Lip Balm Label Design

Design a label for a Lavender-Mint lip balm. We make high-quality natural essential oil products. Please use the old label as an example of what exists. The label should include purple. The final design should be eye-catching and distinct. The file should be in an AI file.

Here is the information that should be included on the label:
1) ingredients:Theobroma Cacao (Cocoa) Seed Butter, Theobroma grandiflorum Ultra Refined Butter, beesewax, Calendula Officinalis Flower Oil, Prunus Amygdalus Dulcis (Sweet Almond) Oil, cetyl alcohol and Tocopherol. Lavandula Angustifolia (Lavender) Oil and Mentha Piperita (Peppermint) Oil.

2) www.kelvorascent.com

3) Brand name and logo: K. Velora Aromatherapy (logo is attached- you can use with form)

```html
<!DOCTYPE html>
<html lang="en">
<head>
<meta charset="utf-8">
<title>K. Velora Aromatherapy – Lavender-Mint Lip Balm Label</title>
<link rel="stylesheet" href="https://fonts.googleapis.com/css2?family=Open+Sans:wght@400;600&display=swap">
<style>
  :root {
    --purple: #7b35b4;
    --purple-light: #b083d8;
    --ink: #4a4a4a;
    --dieline: #c8c8c8;
    --paper: #ffffff;
    --photo-dark: #a9a9a9;
    --photo-mid: #d6d6d6;
    --photo-light: #f2f2f2;
  }
  * { margin: 0; padding: 0; box-sizing: border-box; }
  html, body { width: 1200px; height: 1000px; overflow: hidden; background: var(--paper); }
  body { font-family: "Open Sans", Arial, sans-serif; color: var(--ink); position: relative; }

  .dieline { position: absolute; left: 0; top: 0; }

  .label { position: absolute; left: 48px; top: 153px; width: 725px; height: 559px; }

  .front-panel { position: absolute; left: 0; top: 0; width: 380px; height: 559px; }
  .lips-photo {
    position: absolute; left: 1px; top: 1px; width: 379px; height: 420px;
    background:
      radial-gradient(ellipse 150px 42px at 200px 115px, var(--photo-dark) 0%, rgba(169,169,169,0) 100%),
      radial-gradient(ellipse 40px 120px at 12px 170px, #c4c4c4 0%, rgba(196,196,196,0) 100%),
      linear-gradient(180deg, var(--photo-light) 0%, var(--photo-mid) 40%, #e6e6e6 62%, var(--paper) 100%);
  }
  .brand-name {
    position: absolute; left: 0; width: 380px; top: 352px; text-align: center;
    font-size: 28px; font-weight: 600; color: var(--purple); line-height: 1.12;
  }
  .tagline {
    position: absolute; left: 0; width: 380px; top: 424px; text-align: center;
    font-size: 11px; letter-spacing: .2px; color: var(--ink);
  }
  .product-band {
    position: absolute; left: 1px; width: 379px; top: 457px; height: 34px;
    background: var(--purple); color: #fff; font-size: 14px; letter-spacing: .3px;
    display: flex; align-items: center; justify-content: center;
  }
  .net-weight {
    position: absolute; left: 0; width: 380px; top: 509px; text-align: center; font-size: 12px;
  }

  .web-band {
    position: absolute; left: 380px; top: 0; width: 38px; height: 559px; background: var(--purple);
  }
  .web-address {
    position: absolute; left: 50%; top: 50%; transform: translate(-50%, -50%) rotate(-90deg);
    white-space: nowrap; color: #fff; font-size: 19px; letter-spacing: .4px;
  }

  .ingredients-panel { position: absolute; left: 418px; top: 0; width: 199px; height: 559px; }
  .ingredients {
    position: absolute; left: 50%; top: 50%; width: 450px;
    transform: translate(-50%, -50%) rotate(-90deg);
    text-align: center; font-size: 12.5px; line-height: 1.55; color: var(--ink);
  }
  .ingredients h2 { font-size: 13px; font-weight: 400; letter-spacing: .3px; }

  .floral-pattern {
    position: absolute; left: 617px; top: 1px; width: 107px; height: 557px;
    background: linear-gradient(90deg, #e4d2f2 0%, var(--purple-light) 55%, var(--purple-light) 100%);
  }
</style>
</head>
<body>
  <svg class="dieline" width="1200" height="1000" viewBox="0 0 1200 1000" aria-hidden="true">
    <path d="M48 153 H140 V70 Q140 48 162 48 H308 Q330 48 330 70 V153 H772 V712 H48 Z"
          fill="none" stroke="var(--dieline)" stroke-width="1"/>
  </svg>

  <main class="label">
    <section class="front-panel">
      <div class="lips-photo" role="img" aria-label="Soft black-and-white close-up photograph of lips and a fingertip, fading to white"></div>
      <div class="brand-name">K. Velora<br>Aromatherapy</div>
      <p class="tagline">FOR INSTANT MOISTURE LIP</p>
      <div class="product-band">LAVENDER-MINT LIP BALM</div>
      <p class="net-weight">100% Natural Lip Balm &nbsp;|&nbsp; NET WT .15 OZ / 4G</p>
    </section>

    <section class="web-band">
      <span class="web-address">www.kelvorascent.com</span>
    </section>

    <section class="ingredients-panel">
      <div class="ingredients">
        <h2>INGREDIENTS</h2>
        <p>Theobroma Cacao (Cocoa) Seed Butter, Theobroma grandiflorum Ultra Refined Butter, beesewax, Calendula Officinalis Flower Oil, Prunus Amygdalus Dulcis (Sweet Almond) Oil, cetyl alcohol and Tocopherol. Lavandula Angustifolia (Lavender) Oil and Mentha Piperita (Peppermint) Oil.</p>
      </div>
    </section>

    <div class="floral-pattern" role="img" aria-label="Decorative lavender petal pattern along the panel edge"></div>
  </main>
</body>
</html>
```